TRVL-NINE Web Design

We are a Health, Safety, Environmental & Quality Recruitment Agency, our clients are major corporate Mining, Oil & Gas and Engineering companies. We have offices in Perth & Melbourne, Australia

The website should be very functional & easy to navigate

BUT REALLY LOOKING FOR WOW FACTOR!

Please Note: TRVL CORPORATE IS OUR OLD COMPANY THE NEW ONE IS "TRVL-NINE" 

Some idea's from our competitors:

http://www.guardlinepeak.com.au/
http://www.vantagehiring.com.au/
http://www.brightpick.com.au/
http://www.kovastaffing.co.uk/
http://www.jobmarrow.com/health-safety-environment-jobs

Would love to see some of our valued clients and there logos

still looking for wow factor

Industry/Entity Type

Mining

Requirements
Must have
• A place where candidates can upload there resumes & other contact details
• eg: http://www.guardlinepeak.com.au/candidates/register-your-resume/
• A place we can load jobs on to eg: http://www.guardlinepeak.com.au/vacancies/
• Contact details:
• Perth: 12 Kestrel Ave, West Perth, Western Australia 6005
• t: 08 7153 4406 | f: 08 7153 4470 |
• Melbourne: Level 1, 218 Arbour Lane, Melbourne, Victoria 3000
• t: 03 6214 5072| f: 03 6231 4095 |
• e: dennisk@trvlnine.com.au | w: http://www.trvlnine.com.au

```html
<!DOCTYPE html>
<html lang="en">
<head>
<meta charset="utf-8">
<title>TRVL Corporate – HSEQ Recruitment</title>
<link rel="stylesheet" href="https://fonts.googleapis.com/css2?family=Comfortaa:wght@300;700&family=Ubuntu:wght@300;400&display=swap">
<style>
:root{
  --blue:#0a78b6;
  --blue-dark:#0b65a0;
  --blue-field:#1c92d2;
  --blue-btn:#27aee6;
  --panel-grey:#e8e8e8;
  --charcoal:#4a4a4a;
  --card:#2f2f2f;
  --orange:#f0a01e;
  --cyan:#23a6e4;
  --white:#ffffff;
  --text-grey:#3c3c3c;
}
*{box-sizing:border-box;margin:0;padding:0}
html,body{width:819px;height:1200px;overflow:hidden}
body{position:relative;font-family:'Ubuntu',sans-serif;font-weight:300;background:var(--charcoal);color:var(--white)}
.abs{position:absolute}
a{color:inherit;text-decoration:none}

/* header */
.site-header{left:0;top:0;width:819px;height:98px;background:var(--blue)}
.brand-panel{left:0;top:0;width:394px;height:98px}
.brand-mark{left:34px;top:14px;width:66px;height:66px;background:var(--blue)}
.brand-name{left:116px;top:26px;font-family:'Comfortaa',sans-serif;font-weight:300;font-size:33px;color:var(--blue-dark);letter-spacing:.5px}
.search-field{left:456px;top:9px;width:235px;height:21px;background:var(--blue-field);border-radius:3px 0 0 3px;font-size:9px;padding:5px 10px;color:#cfe9f7}
.search-btn{left:690px;top:9px;width:81px;height:21px;background:var(--blue-btn);border-radius:0 3px 3px 0;font-size:11px;font-weight:400;text-align:center;line-height:21px}
.nav-top{top:44px;right:49px;font-size:9px}
.nav-top span{margin-left:22px}
.nav-main{top:68px;left:394px;width:377px;font-size:10px;display:flex;justify-content:space-between}

/* hero */
.hero{left:0;top:98px;width:819px;height:364px;background:linear-gradient(180deg,#1b2a3f 0%,#31465f 35%,#5b5a4c 62%,#2a2418 78%,#0c0c0c 100%)}
.hero-arrow{top:240px}
.caption-band{left:0;top:419px;width:819px;height:43px;background:rgba(30,30,30,.75);text-align:center;font-size:28px;letter-spacing:2px;line-height:43px}

/* intro panels */
.intro{left:0;top:462px;width:819px;height:238px;background:var(--panel-grey)}
.intro-clip{top:510px;width:188px;height:118px;overflow:hidden}
.intro-bubble{width:188px;height:188px;border-radius:50%;background:var(--white);color:var(--text-grey);text-align:center;padding:30px 14px 0}
.intro-title{font-family:'Comfortaa',sans-serif;font-weight:700;font-size:13px;color:var(--blue);margin-bottom:10px;white-space:nowrap}
.intro-text{font-size:10.5px;line-height:14px}
.intro-btn{top:624px;width:221px;height:34px;background:var(--blue);border-radius:4px;text-align:center;line-height:34px;font-size:12px;font-weight:400;box-shadow:0 5px 4px -2px rgba(0,0,0,.45)}

/* feature band */
.features{left:0;top:700px;width:819px;height:210px;background:linear-gradient(180deg,#0b6fae,#0a7dbd)}
.feature-divider{top:730px;width:1px;height:137px;background:rgba(255,255,255,.15)}
.feature-title{top:742px;font-family:'Comfortaa',sans-serif;font-weight:700;font-size:14px;text-decoration:underline;text-align:center;width:200px}
.feature-text{top:785px;width:190px;font-size:12.5px;line-height:15.5px;text-align:justify}
.feature-tab{top:876px}
.feature-more{top:895px;width:172px;text-align:center;font-size:12px;color:var(--orange);font-weight:400}

/* vacancies */
.vacancies-title{left:0;top:954px;width:819px;text-align:center;font-family:'Comfortaa',sans-serif;font-weight:700;font-size:19px;letter-spacing:1px}
.job-card{top:1014px;width:219px;height:112px;background:var(--card);border-radius:5px;text-align:center;padding:14px 8px 0}
.job-title{font-size:12px;font-weight:400;line-height:15px}
.job-pay{color:var(--cyan);font-size:10.5px}
.job-text{font-size:9.8px;line-height:13px;color:#cfcfcf;margin-top:9px;letter-spacing:.2px}
.job-link{position:absolute;right:18px;bottom:9px;color:var(--orange);font-size:10.5px;font-weight:400}
.slide-tab{top:1042px;width:29px;height:58px;background:#3a3a3a}

/* footer */
.site-footer{left:0;top:1170px;width:819px;height:30px;background:var(--blue-dark);font-size:8.5px;line-height:30px;padding:0 22px;display:flex;justify-content:space-between}
.site-footer .legal{padding-right:22px}
</style>
</head>
<body>

<header class="abs site-header">
  <svg class="abs brand-panel" width="394" height="98" viewBox="0 0 394 98"><polygon points="0,0 374,0 394,36 374,72 374,98 0,98" fill="#fff"/></svg>
  <div class="abs brand-mark"></div>
  <div class="abs brand-name">trvl corporate</div>
  <div class="abs search-field">Type Here . . .</div>
  <div class="abs search-btn">SEARCH</div>
  <nav class="abs nav-top"><span>HOME</span><span>|</span><span>LOGIN</span><span>|</span><span>REGISTER</span></nav>
  <nav class="abs nav-main"><span>ABOUT US</span><span>|</span><span>FOR CANDIDATES</span><span>|</span><span>FOR EMPLOYERS</span><span>|</span><span>SECTORS</span><span>|</span><span>SEARCH</span></nav>
</header>

<section class="abs hero" role="img" aria-label="Night photograph of an industrial power station with cooling tower and cranes reflected in water"></section>
<svg class="abs hero-arrow" style="left:22px" width="18" height="48" viewBox="0 0 18 48"><polygon points="18,0 0,24 18,48 13,24" fill="#c8ccd2" opacity=".85"/></svg>
<svg class="abs hero-arrow" style="left:769px" width="18" height="48" viewBox="0 0 18 48"><polygon points="0,0 18,24 0,48 5,24" fill="#c8ccd2" opacity=".85"/></svg>
<div class="abs caption-band">CAPTION HERE</div>

<section class="abs intro"></section>
<div class="abs intro-clip" style="left:58px"><div class="intro-bubble">
  <h2 class="intro-title">ABOUT US</h2>
  <p class="intro-text">Australia's number one group in health, safety, environmental and quality recruitment.</p>
</div></div>
<div class="abs intro-clip" style="left:316px"><div class="intro-bubble">
  <h2 class="intro-title">FOR CANDIDATES</h2>
  <p class="intro-text">TRVL Corporate recognises the importance to align the right opportunity that best suits individual needs.</p>
</div></div>
<div class="abs intro-clip" style="left:572px"><div class="intro-bubble" style="padding:30px 20px 0">
  <h2 class="intro-title">FOR EMPOLYERS</h2>
  <p class="intro-text">Finding the right people in today's market place is becoming increasingly difficult by the day. Let us help.</p>
</div></div>
<a class="abs intro-btn" style="left:41px">READ MORE</a>
<a class="abs intro-btn" style="left:299px">READ MORE</a>
<a class="abs intro-btn" style="left:554px">READ MORE</a>

<section class="abs features"></section>
<div class="abs feature-divider" style="left:277px"></div>
<div class="abs feature-divider" style="left:542px"></div>
<h2 class="abs feature-title" style="left:43px">SECTORS</h2>
<h2 class="abs feature-title" style="left:312px">SEARCH</h2>
<h2 class="abs feature-title" style="left:564px">REGISTER</h2>
<p class="abs feature-text" style="left:51px">TRVL Corporate Specialise in the Mining, Oil, Gas, Engineering and Construction Sectors.</p>
<p class="abs feature-text" style="left:317px">Our vacancies are posted on our website as soon as we receive them. Search here for our latest jobs.</p>
<p class="abs feature-text" style="left:581px">Register so we can contact you to discuss your requirements and provide you with the details of our latest opportunities.</p>
<svg class="abs feature-tab" style="left:68px" width="172" height="34" viewBox="0 0 172 34"><polygon points="0,34 86,2 172,34" fill="#4a4a4a"/></svg>
<svg class="abs feature-tab" style="left:330px" width="172" height="34" viewBox="0 0 172 34"><polygon points="0,34 86,2 172,34" fill="#4a4a4a"/></svg>
<svg class="abs feature-tab" style="left:586px" width="172" height="34" viewBox="0 0 172 34"><polygon points="0,34 86,2 172,34" fill="#4a4a4a"/></svg>
<a class="abs feature-more" style="left:66px">READ MORE</a>
<a class="abs feature-more" style="left:327px">READ MORE</a>
<a class="abs feature-more" style="left:584px">READ MORE</a>

<h2 class="abs vacancies-title">LATEST VACANCIES</h2>
<div class="abs slide-tab" style="left:11px;border-radius:29px 0 0 29px"></div>
<div class="abs slide-tab" style="left:775px;border-radius:0 29px 29px 0"></div>
<svg class="abs" style="left:20px;top:1059px" width="14" height="24" viewBox="0 0 14 24"><polyline points="11,2 4,12 11,22" fill="none" stroke="#9a9a9a" stroke-width="3"/></svg>
<svg class="abs" style="left:781px;top:1059px" width="14" height="24" viewBox="0 0 14 24"><polyline points="3,2 10,12 3,22" fill="none" stroke="#9a9a9a" stroke-width="3"/></svg>

<article class="abs job-card" style="left:51px">
  <h3 class="job-title">HSE Advisors ( Barrow Island)</h3>
  <div class="job-pay">Negotiable</div>
  <p class="job-text">We are now recruiting experienced Health and Saftey advisors to work</p>
  <a class="job-link">Details &gt;&gt;</a>
</article>
<article class="abs job-card" style="left:296px">
  <h3 class="job-title">HSE Advisors</h3>
  <div class="job-pay">Negotiable</div>
  <p class="job-text">We are recruiting for an experienced Health &amp; Safety Advisor to</p>
  <a class="job-link">Details &gt;&gt;</a>
</article>
<article class="abs job-card" style="left:542px;padding:12px 6px 0">
  <h3 class="job-title">Underground Safety &amp; Training Coordinators <span class="job-pay">&nbsp;Negotiable</span></h3>
  <p class="job-text" style="margin-top:8px;letter-spacing:0">We are currently seeking a suitably experi-enced Environmental, Health, Safety and</p>
  <a class="job-link">Details &gt;&gt;</a>
</article>

<footer class="abs site-footer">
  <span>Home | Rss Feed | Login | Register | Privacy policy | Legal | Testimonials</span>
  <span class="legal">TRVL Corporate Pty Ltd &nbsp;© 2013-2014</span>
</footer>

</body>
</html>
```